Tapmark Volley - App Graphics Design

Context
-
Our company has launched an inplay mobile game app - where players can predict in real-time what will happen next during live football matches.
The game is called Tapmark Volley and currently has the following online resources:
Brightwall Page: http://www.brightwall-social.example/pages/Tapmark-Volley/918273645501928
iOS App: http://apps.orchardshelf.example/us/app/tapmark-volley/id807162534?mt=8
Android App: https://store.greenlanta.example/apps/details?id=com.tapmarkvolley.android
The Project
-
This project involves creating enhanced graphics for the app - based on the current functional layout (see screenshots).
The graphics should be consistent throughout the game, and the design should improve the look and feel for the end user.
The designs should do as follows:
- Continue to enable the full functionality shown in the current screenshots
- Feel free to change any / all colour schemes / layouts / designs / graphics
- Look good to a sports fan user
Updates
I have just increased the 1st prize for this project by £200 to £460 - looking forward to seeing your app designs.
Just added football shirt icons, and the "Tapmark Volley" logo to assist with designs.
Project Deadline Extended
Reason: Extended to allow for revised submissions
Target Market(s)
Global Football Fans, low education level
Industry/Entity Type
It Company
Look and feel
Each slider illustrates characteristics of the customer's brand and the style your logo design should communicate.

```html
<!DOCTYPE html>
<html lang="en">
<head>
<meta charset="utf-8">
<title>Tapmark Volley – How to play</title>
<link rel="stylesheet" href="https://fonts.googleapis.com/css2?family=Roboto+Condensed:wght@400;700&display=swap">
<style>
  :root {
    --page-bg: #101410;
    --screen-black: #050605;
    --status-text: #f2f2f2;
    --pitch-deep: #0f2a0c;
    --pitch-mid: #23521a;
    --pitch-light: #3f7d2a;
    --panel-bg: #2b2019;
    --panel-edge: #3b2d22;
    --panel-title: #f4efe8;
    --panel-text: #b89f86;
    --panel-number: #c7ae93;
    --tab-bg: #0b0b0a;
    --tab-active: #1c3d14;
    --tab-active-text: #5fae3c;
    --tab-text: #3a3a36;
    --ball-light: #d9d9d9;
    --ball-dark: #3a3a3a;
  }
  * { margin: 0; padding: 0; box-sizing: border-box; }
  html, body {
    width: 1200px; height: 1153px; overflow: hidden;
    background: var(--page-bg);
    font-family: "Roboto Condensed", "Arial Narrow", sans-serif;
  }
  .app-screen {
    position: absolute; left: 248px; top: 48px;
    width: 320px; height: 480px;
    transform: scale(2.2); transform-origin: 0 0;
    background: var(--screen-black);
    overflow: hidden;
  }
  .status-bar {
    position: absolute; left: 0; top: 0; width: 320px; height: 20px;
    background: #000; color: var(--status-text);
    font-size: 11px; font-weight: 700; letter-spacing: .3px;
    display: flex; align-items: center; padding: 0 6px;
  }
  .status-bar .signal { display: flex; align-items: flex-end; gap: 1px; height: 9px; margin-right: 4px; }
  .status-bar .signal i { display: block; width: 2px; background: var(--status-text); }
  .status-bar .clock { position: absolute; left: 0; right: 0; text-align: center; }
  .status-bar .battery {
    position: absolute; right: 8px; top: 6px; width: 20px; height: 9px;
    border: 1px solid var(--status-text); border-radius: 2px; padding: 1px;
  }
  .status-bar .battery::before { content: ""; display: block; width: 100%; height: 100%; background: var(--status-text); }
  .status-bar .battery::after { content: ""; position: absolute; right: -3px; top: 2px; width: 2px; height: 3px; background: var(--status-text); }
  .pitch {
    position: absolute; left: 0; top: 20px; width: 320px; height: 413px;
    background: radial-gradient(ellipse at 50% 55%, var(--pitch-mid) 0%, var(--pitch-deep) 75%);
  }
  .pitch-grass {
    position: absolute; left: 0; bottom: 0; width: 320px; height: 46px;
    background: linear-gradient(to bottom, var(--pitch-light), var(--pitch-mid) 60%, var(--pitch-deep));
  }
  .close-button {
    position: absolute; left: 289px; top: 42px; width: 16px; height: 16px;
    border-radius: 50%; background: #2a2a27; border: 1px solid #4a4a44;
  }
  .help-panel {
    position: absolute; left: 22px; top: 54px; width: 278px; height: 326px;
    background: var(--panel-bg); border: 1px solid var(--panel-edge);
    box-shadow: 0 2px 10px rgba(0,0,0,.6);
  }
  .help-title {
    position: absolute; left: 20px; top: 20px;
    display: flex; align-items: center; gap: 7px;
    color: var(--panel-title); font-size: 14px; font-weight: 700;
  }
  .help-steps { list-style: none; position: absolute; left: 30px; top: 70px; width: 230px; }
  .help-steps li {
    display: flex; gap: 10px; height: 46px;
    color: var(--panel-text); font-size: 8px; font-weight: 700; line-height: 1.3;
  }
  .help-steps .step-number { color: var(--panel-number); font-size: 14px; width: 12px; line-height: 1; flex: none; }
  .tab-bar {
    position: absolute; left: 0; top: 433px; width: 320px; height: 47px;
    background: var(--tab-bg); display: flex;
  }
  .tab { flex: 1; display: flex; flex-direction: column; align-items: center; justify-content: flex-end; padding-bottom: 5px; gap: 4px; color: var(--tab-text); font-size: 7px; }
  .tab-home { flex: 0 0 58px; background: var(--tab-active); color: var(--tab-active-text); }
  .tab-spacer { flex: 0 0 70px; }
  .tab .tab-icon { width: 12px; height: 12px; }
  .match-ball {
    position: absolute; left: 121px; top: 395px; width: 76px; height: 76px; border-radius: 50%;
    background: radial-gradient(circle at 38% 35%, var(--ball-light), var(--ball-dark) 85%);
  }
</style>
</head>
<body>
  <main class="app-screen">
    <header class="status-bar">
      <span class="signal"><i style="height:3px"></i><i style="height:5px"></i><i style="height:7px"></i><i style="height:9px"></i></span>
      <span>CARRIER&nbsp;3G</span>
      <span class="clock">12:00</span>
      <span class="battery"></span>
    </header>

    <section class="pitch" role="img" aria-label="Floodlit grass pitch backdrop">
      <div class="pitch-grass"></div>
    </section>

    <button class="close-button" aria-label="Close"></button>

    <section class="help-panel">
      <h1 class="help-title">
        <svg width="16" height="16" viewBox="0 0 16 16" aria-hidden="true">
          <path d="M8 1.5a6.5 6 0 1 1-3.4 11.1L2 14.5l.9-3.1A6 6 0 0 1 8 1.5z" fill="none" stroke="#f4efe8" stroke-width="1.2"/>
          <text x="8" y="10.8" text-anchor="middle" font-size="8" font-weight="700" fill="#f4efe8" font-family="Roboto Condensed, sans-serif">?</text>
        </svg>
        How to play
      </h1>
      <ol class="help-steps">
        <li><span class="step-number">1.</span><span>Select the match you want to make your prediction on.</span></li>
        <li><span class="step-number">2.</span><span>Give a thumbs - up to the outcome you predict will happen.</span></li>
        <li><span class="step-number">3.</span><span>You will GAIN points if your predicted outcome becomes MORE LIKELY.</span></li>
        <li><span class="step-number">4.</span><span>You will LOSE points if your predicted outcome becomes LESS LIKELY.</span></li>
        <li><span class="step-number">5.</span><span>You can change your prediction at any time before or during the match.</span></li>
      </ol>
    </section>

    <nav class="tab-bar">
      <div class="tab tab-home">
        <svg class="tab-icon" viewBox="0 0 12 12" aria-hidden="true"><path d="M6 1 1 6h1.5v5h3V8h1v3h3V6H11z" fill="#5fae3c"/></svg>
        <span>Home</span>
      </div>
      <div class="tab">
        <svg class="tab-icon" viewBox="0 0 12 12" aria-hidden="true"><path d="M6 1l1.5 3.3 3.5.4-2.6 2.4.7 3.5L6 8.8 2.9 10.6l.7-3.5L1 4.7l3.5-.4z" fill="#3a3a36"/></svg>
        <span>Rankings</span>
      </div>
      <div class="tab-spacer"></div>
      <div class="tab">
        <svg class="tab-icon" viewBox="0 0 12 12" aria-hidden="true"><rect x="1.5" y="1.5" width="9" height="9" fill="none" stroke="#3a3a36" stroke-width="1.4"/><rect x="4.5" y="4.5" width="3" height="3" fill="#3a3a36"/></svg>
        <span>Store</span>
      </div>
      <div class="tab">
        <svg class="tab-icon" viewBox="0 0 12 12" aria-hidden="true"><path d="M1 2h7v5H4l-2 2V7H1zM9 4h2v5h-1v2l-2-2H5V8h4z" fill="#3a3a36"/></svg>
        <span>Social</span>
      </div>
    </nav>

    <div class="match-ball" role="img" aria-label="Football illustration"></div>
  </main>
</body>
</html>
```